Redesign of an insurance website

Attached is an insurance website that I need to redesign. Currently the website is too dark. I like for example www.brambleshield.com . Could you make the website lighter and change the structure a little so that it is more user friendly?

Industry/Entity Type

Insurance

Number of Pages Required

4 page

```html
<!DOCTYPE html>
<html lang="en">
<head>
<meta charset="utf-8">
<title>Krytoplan.cz — Financial &amp; Insurance Solutions</title>
<link href="https://fonts.googleapis.com/css2?family=Montserrat:wght@300;400;500;600;700&display=swap" rel="stylesheet">
<style>
:root{
  --navy:#1b2b5c;
  --navy-deep:#0f1f47;
  --topbar:#1d2c55;
  --teal:#117a6a;
  --teal-dark:#0d6457;
  --orange:#f4821f;
  --text:#5f6570;
  --muted:#8a9099;
  --line:#dfe3e8;
  --soft:#f4f6f9;
  --white:#ffffff;
}
*{box-sizing:border-box;margin:0;padding:0}
html,body{width:1200px;height:4235px;overflow:hidden}
body{position:relative;background:var(--white);font-family:'Montserrat',sans-serif;color:var(--text);font-size:12.5px;line-height:1.7}
.abs{position:absolute}
a{color:inherit;text-decoration:none}

/* top bar */
.topbar{left:0;top:0;width:1200px;height:42px;background:var(--topbar);color:#cfd6e6;font-size:12px}
.topbar .welcome{left:51px;top:11px}
.topbar .social{left:505px;top:14px;display:flex;gap:46px}
.topbar .social span{width:12px;height:12px;border-radius:50%;background:#cfd6e6;display:block}
.topbar .search{left:1123px;top:12px}

/* header */
.header{left:0;top:42px;width:1200px;height:119px;background:var(--white)}
.logo{font-weight:700;color:var(--navy);font-size:27px;letter-spacing:.5px}
.header .logo{left:51px;top:40px}
.header .contact{color:#fff;font-size:12.5px;line-height:1.4}
.header .contact small{display:block;font-size:11px;color:#cfe7e2}
.header .contact svg{position:absolute;left:-40px;top:2px}
.btn{display:inline-block;font-weight:600;font-size:12px;letter-spacing:.5px;text-align:center}
.quote{left:1003px;top:45px;width:112px;height:35px;line-height:35px;background:var(--orange);color:#fff;border-radius:2px}

/* hero */
.hero{left:0;top:161px;width:1200px;height:472px}
.hero-photo{left:0;top:0;width:1200px;height:472px;background:linear-gradient(100deg,#f1f4f7 0%,#e6ecf2 38%,#b9c6d3 62%,#6f7f93 80%,#c8b8a4 100%)}
.nav{left:0;top:20px;width:1200px;display:flex;justify-content:center;gap:46px;font-size:12px;font-weight:500;color:var(--navy);letter-spacing:.3px}
.hero .kicker{left:160px;top:150px;font-size:17px;font-weight:600;color:var(--navy);letter-spacing:.3px}
.hero h1{left:56px;top:180px;font-size:56px;font-weight:700;color:var(--teal);letter-spacing:.5px;line-height:1.2}
.hero p{left:187px;top:253px;width:440px;text-align:center;font-size:13px;color:var(--text)}
.hero .view{left:282px;top:342px;width:150px;height:35px;line-height:33px;border:1px solid var(--navy);color:var(--navy)}
.hero .chat{left:1108px;top:368px;width:28px;height:28px;border-radius:50%;background:var(--orange)}

/* section heads */
.section-title{font-weight:600;color:var(--teal);font-size:27px}
.heading{font-weight:600;color:var(--navy);font-size:28px;line-height:1.25}
.eyebrow{font-weight:600;color:var(--teal);font-size:16px}

/* services */
.services-title{left:0;top:735px;width:1200px;text-align:center}
.services-intro{left:280px;top:782px;width:640px;text-align:center}
.service{width:320px}
.service .icon{position:absolute;left:0;top:0;width:34px;height:34px;border-radius:50%;border:1px solid var(--line);display:flex;align-items:center;justify-content:center}
.service h3{margin-left:56px;font-size:15px;font-weight:600;color:var(--teal);line-height:1.3}
.service p{margin-left:56px;margin-top:6px;font-size:12.5px}

/* plan */
.plan{left:0;top:1180px;width:1200px;height:565px;background:var(--soft)}
.chart{left:0;top:1320px}
.plan-text{left:613px;top:1295px;width:560px}
.plan-text p{margin-top:14px}
.learn{margin-top:28px;width:128px;height:28px;line-height:26px;border:1px solid var(--navy);color:var(--navy);font-size:11px}

/* about */
.about-left{left:51px;top:1860px;width:490px}
.about-left .we{font-size:17px;font-weight:600;color:var(--navy)}
.about-left .we b{color:var(--teal)}
.about-left p{margin-top:16px}
.feature-sm{width:250px}
.feature-sm h4{font-size:15px;font-weight:600;color:var(--teal)}
.feature-sm p{margin-top:6px}
.photo{background:linear-gradient(180deg,#eef1f4,#c9d1da)}

/* band */
.band{left:0;top:2437px;width:1200px;height:254px;background:linear-gradient(90deg,var(--teal-dark),var(--teal) 50%,var(--teal-dark))}
.band h2{left:0;top:50px;width:1200px;text-align:center;color:#fff;font-size:27px;font-weight:600}
.band p{left:330px;top:100px;width:540px;text-align:center;color:#d9efe9;font-size:13px}
.band .buy{left:545px;top:163px;width:110px;height:32px;line-height:32px;background:#fff;color:var(--navy)}

/* why */
.why-photo{left:0;top:2691px;width:556px;height:339px;background:linear-gradient(120deg,#dfe5ec,#a5b4c5 60%,#6a7a90)}
.why-text{left:582px;top:2712px;width:580px}
.why-text .heading{font-size:30px}
.why-text p.lead{margin-top:14px}
.why-item{width:250px}
.why-item svg{position:absolute;left:0;top:2px}
.why-item h4{margin-left:62px;font-size:15px;font-weight:600;color:var(--teal)}
.why-item p{margin-left:62px;margin-top:4px}

/* callback + faq */
.form-col{left:51px;top:3200px;width:534px}
.form-col p,.faq-col p.lead{margin-top:14px}
.field{border:1px solid var(--line);height:37px;padding:9px 12px;font-size:12px;color:var(--muted)}
.submit{left:51px;top:3620px;width:124px;height:32px;line-height:32px;background:var(--navy);color:#fff;font-size:11.5px}
.faq-col{left:669px;top:3200px;width:490px}
.faq-item{font-size:12.5px;color:var(--navy);display:flex;align-items:center;gap:16px}
.faq-item .mark{width:18px;height:18px;display:flex;align-items:center;justify-content:center;color:var(--navy);font-weight:600}
.faq-item.open .mark{background:var(--navy);color:#fff}
.faq-item.open span.q{color:var(--teal)}

/* footer */
.footer{left:0;top:3756px;width:1200px;height:479px;background:linear-gradient(135deg,var(--navy-deep),#14295a 60%,var(--navy-deep));color:#c3cbdc}
.footer .logo{color:#fff}
.footer h5{color:#fff;font-size:14px;font-weight:600;letter-spacing:.4px}
.footer .col{font-size:12.5px}
.newsletter{border:1px solid #53628a;height:32px;padding:6px 12px;font-size:11.5px;color:#c3cbdc}
.footer .links div{margin-top:10px}
.footer .rule{left:51px;top:339px;width:1098px;height:1px;background:#2f4174}
.footer .copy{left:0;top:410px;width:1200px;text-align:center;font-size:12px}
</style>
</head>
<body>

<div class="abs topbar">
  <div class="abs welcome">Welcome to Krytoplan.cz</div>
  <div class="abs social"><span></span><span></span><span></span><span></span></div>
  <svg class="abs search" width="16" height="16" viewBox="0 0 16 16"><circle cx="7" cy="7" r="5" fill="none" stroke="#cfd6e6" stroke-width="2"/><line x1="11" y1="11" x2="15" y2="15" stroke="#cfd6e6" stroke-width="2"/></svg>
</div>

<header class="abs header">
  <div class="abs logo">KRYTOPLAN.CZ</div>
  <svg class="abs" style="left:0;top:0" width="1200" height="119">
    <polygon points="318,0 345,0 378,119 351,119" fill="var(--orange)"/>
    <polygon points="345,0 1200,0 1200,119 378,119" fill="var(--teal)"/>
  </svg>
  <div class="abs contact" style="left:505px;top:42px">
    <svg width="22" height="22" viewBox="0 0 24 24"><path d="M5 3h4l2 5-2.5 1.5a11 11 0 0 0 6 6L16 13l5 2v4a2 2 0 0 1-2 2A16 16 0 0 1 3 5a2 2 0 0 1 2-2z" fill="none" stroke="#fff" stroke-width="1.5"/></svg>
    (+420) 555-014-230<small>We are open 9 am - 10pm</small>
  </div>
  <div class="abs contact" style="left:780px;top:42px">
    <svg width="24" height="20" viewBox="0 0 24 20"><rect x="2" y="3" width="20" height="14" fill="none" stroke="#fff" stroke-width="1.5"/><path d="M2 3l10 8 10-8" fill="none" stroke="#fff" stroke-width="1.5"/></svg>
    hello@krytoplan.cz<small>You can mail us</small>
  </div>
  <a class="abs btn quote">GET A QUOTE</a>
</header>

<section class="abs hero">
  <div class="abs hero-photo" role="img" aria-label="Photo of two smiling business colleagues reviewing a plan together in a bright office"></div>
  <nav class="abs nav"><a>HOME</a><a>ABOUT US</a><a>CASES</a><a>SERVICES</a><a>PRODUCTS</a><a>BLOG</a><a>SHOP</a><a>CONTACT</a></nav>
  <div class="abs kicker">WE PROVIDE BEST FINANCIAL SOLUTIONS</div>
  <h1 class="abs">FOR YOUR BUSINESS</h1>
  <p class="abs">We have over 25 year's of experience in Finance and Business management so we can make your business more successful you can trust us.</p>
  <a class="abs btn view">VIEW SERVICES</a>
  <div class="abs chat"></div>
</section>

<h2 class="abs section-title services-title">Our Services</h2>
<p class="abs services-intro">Fundora amet sit amet, consectetur adipisicing elit, sed do eiusmod tempor incididunt ut labore et dolore magna aliqua. Ut enim ad minim veniam, quis nostrud exercitation ullamco.</p>

<div class="abs service" style="left:56px;top:876px">
  <div class="icon"><svg width="16" height="16" viewBox="0 0 16 16"><rect x="3" y="2" width="10" height="12" fill="none" stroke="#6b7380"/><line x1="5" y1="6" x2="11" y2="6" stroke="#6b7380"/><line x1="5" y1="9" x2="11" y2="9" stroke="#6b7380"/></svg></div>
  <h3>Financial Planning</h3><p>Fundora consectetur adipiscing elit, sed do eiusmod tempor incididunt</p>
</div>
<div class="abs service" style="left:429px;top:876px">
  <div class="icon"><svg width="16" height="16" viewBox="0 0 16 16"><rect x="2" y="5" width="12" height="8" fill="none" stroke="#6b7380"/><circle cx="8" cy="9" r="2" fill="none" stroke="#6b7380"/></svg></div>
  <h3>Cash Investment</h3><p>Fundora consectetur adipiscing elit, sed do eiusmod tempor incididunt</p>
</div>
<div class="abs service" style="left:805px;top:876px">
  <div class="icon"><svg width="16" height="16" viewBox="0 0 16 16"><rect x="2" y="5" width="12" height="9" fill="none" stroke="#6b7380"/><path d="M6 5V3h4v2" fill="none" stroke="#6b7380"/></svg></div>
  <h3>Financial Consultancy</h3><p>Fundora consectetur adipiscing elit, sed do eiusmod tempor incididunt</p>
</div>
<div class="abs service" style="left:56px;top:997px">
  <div class="icon"><svg width="16" height="16" viewBox="0 0 16 16"><path d="M2 9l3-3 3 2 3-3 3 3-4 4-2-1-2 1z" fill="none" stroke="#6b7380"/></svg></div>
  <h3>Personal Insurance</h3><p>Fundora consectetur adipiscing elit, sed do eiusmod tempor incididunt</p>
</div>
<div class="abs service" style="left:429px;top:997px">
  <div class="icon"><svg width="16" height="16" viewBox="0 0 16 16"><rect x="3" y="2" width="10" height="12" fill="none" stroke="#6b7380"/><line x1="6" y1="5" x2="10" y2="5" stroke="#6b7380"/></svg></div>
  <h3>Commodities Planning</h3><p>Fundora consectetur adipiscing elit, sed do eiusmod tempor incididunt</p>
</div>
<div class="abs service" style="left:805px;top:997px">
  <div class="icon"><svg width="16" height="16" viewBox="0 0 16 16"><circle cx="8" cy="8" r="5" fill="none" stroke="#6b7380"/><path d="M8 5v3l2 2" fill="none" stroke="#6b7380"/></svg></div>
  <h3>Retirement Planning</h3><p>Fundora consectetur adipiscing elit, sed do eiusmod tempor incididunt</p>
</div>

<section class="abs plan"></section>
<svg class="abs chart" width="565" height="330" viewBox="0 0 565 330" role="img" aria-label="Chart of financial growth peaks">
  <g stroke="#e0e4ea" stroke-width="1">
    <line x1="34" y1="38" x2="560" y2="38"/><line x1="34" y1="99" x2="560" y2="99"/><line x1="34" y1="161" x2="560" y2="161"/><line x1="34" y1="222" x2="560" y2="222"/><line x1="34" y1="284" x2="560" y2="284"/>
  </g>
  <g font-family="Montserrat, sans-serif" font-size="10" fill="#8a9099" text-anchor="end">
    <text x="28" y="41">80</text><text x="28" y="102">60</text><text x="28" y="164">40</text><text x="28" y="225">20</text><text x="28" y="287">0</text>
  </g>
  <g font-family="Montserrat, sans-serif" font-size="10" fill="#8a9099" text-anchor="middle">
    <text x="68" y="302">0</text><text x="155" y="302">2</text><text x="240" y="302">4</text><text x="325" y="302">6</text><text x="415" y="302">8</text><text x="503" y="302">10</text>
  </g>
  <path d="M70 284C120 284 125 126 155 126C185 126 190 284 240 284Z" fill="#1f8a77" opacity=".9"/>
  <path d="M155 284C205 284 210 55 240 55C270 55 275 284 325 284Z" fill="#1e3a6d" opacity=".92"/>
  <path d="M240 284C290 284 295 140 325 140C355 140 360 284 410 284Z" fill="#1f8a77" opacity=".9"/>
  <path d="M330 284C380 284 385 106 415 106C445 106 450 284 500 284Z" fill="#1e3a6d" opacity=".92"/>
  <path d="M418 284C468 284 473 168 503 168C533 168 538 284 560 284Z" fill="#1f8a77" opacity=".9"/>
  <g fill="none" stroke="#fff" stroke-width="1.5">
    <circle cx="113" cy="220" r="4"/><circle cx="198" cy="232" r="4"/><circle cx="283" cy="205" r="4"/><circle cx="370" cy="240" r="4"/><circle cx="460" cy="226" r="4"/>
  </g>
</svg>
<div class="abs plan-text">
  <div class="eyebrow" style="color:var(--teal)">We Provide Best</div>
  <div class="heading">Financial Plan for You</div>
  <p>Fundora amet, ut perspiciatis unde omnis iste natus error sit voluptatem accusantium ipsum dolor sit amet, sitadipiscing elit, sed do eiusmod tempor incididunt ut labore et dolore magna aliqua. Ut enim ad minim veniam, quis nostrud exercitation ullamco laboris nisi ut aliquip ex ea commodo consequat.</p>
  <p>Fundora amet, ut perspiciatis unde omnis iste natus error sit voluptatem accusantium que laudantium, totam rem aperiam, eaque ipsa quae ab illo inventore veritatis ipsum dolor sit amet, consectetur.</p>
  <a class="btn learn">LEARN MORE</a>
</div>

<div class="abs about-left">
  <div class="we">We are <b>KRYTOPLAN.CZ</b></div>
  <div class="heading" style="font-size:26px">Your Complete Financial Solutions</div>
  <p>Fundora amet, consectetur adipiscing elit, sed do eiusmod tempor incididunt ut labore et dolore magna aliqua. Ut enim ad minim iam, quis nostrud exercitation ullamco laboris nisi ut aliquip exea commo consequat. Duis aute irure dolor in reprehenderit.</p>
  <p>Fundora amet, consectetur adipiscing elit, sed do eiusmod tempor incididunt ut labore et dolore magna aliqua enim ad minimiam.</p>
</div>
<div class="abs feature-sm" style="left:613px;top:1937px"><h4>Financial Service</h4><p>Fundora consectetur adipiscing elit, sed do eiusmod tempor incididunt</p></div>
<div class="abs feature-sm" style="left:895px;top:1937px"><h4>Best Consultancy</h4><p>Fundora consectetur adipiscing elit, sed do eiusmod tempor incididunt</p></div>
<div class="abs feature-sm" style="left:613px;top:2033px"><h4>Business Analysis</h4><p>Fundora consectetur adipiscing elit, sed do eiusmod tempor incididunt</p></div>
<div class="abs feature-sm" style="left:895px;top:2033px"><h4>24/7 Support</h4><p>Fundora consectetur adipiscing elit, sed do eiusmod tempor incididunt</p></div>
<div class="abs photo" style="left:220px;top:2160px;width:266px;height:280px" role="img" aria-label="Photo of two businessmen in suits standing side by side"></div>
<div class="abs photo" style="left:678px;top:2160px;width:297px;height:280px" role="img" aria-label="Photo of two businessmen discussing and pointing ahead"></div>

<section class="abs band">
  <h2 class="abs">We Provide Best Financial Services for your Business</h2>
  <p class="abs">We have over 25 year's of experience in Finance and Business management so we can make your business more successful you can trust us and we care about it.</p>
  <a class="abs btn buy">BUY NOW</a>
</section>

<div class="abs why-photo" role="img" aria-label="Photo of a businesswoman with her team meeting around a table"></div>
<div class="abs why-text">
  <div class="eyebrow">Why You</div>
  <div class="heading">Choose Fundora</div>
  <p class="lead">Fundora amet, ut perspiciatis unde omnis iste natus error sit voluptatem accusantium ipsum dolor sit amet, situr adipiscing elit, sed do eiusmod tempor incididunt ut labore et dolore magna.</p>
</div>
<div class="abs why-item" style="left:582px;top:2882px">
  <svg width="36" height="36" viewBox="0 0 36 36"><circle cx="18" cy="18" r="17" fill="none" stroke="#dfe3e8"/><path d="M11 25l4-8 10-6-6 10z" fill="none" stroke="#5f6570" stroke-width="1.3"/></svg>
  <h4>Fast Loan Approval</h4><p>Fundora consectetur adipiscing elit, sed do eiusmod tempor incididnt</p>
</div>
<div class="abs why-item" style="left:898px;top:2882px">
  <svg width="36" height="36" viewBox="0 0 36 36"><circle cx="18" cy="18" r="17" fill="none" stroke="#dfe3e8"/><circle cx="13" cy="15" r="3" fill="none" stroke="#5f6570"/><circle cx="23" cy="15" r="3" fill="none" stroke="#5f6570"/><path d="M8 25c1-4 9-4 10 0M18 25c1-4 9-4 10 0" fill="none" stroke="#5f6570"/></svg>
  <h4>Dedicated Team</h4><p>Fundora consectetur adipiscing elit, sed do eiusmod tempor incididnt</p>
</div>
<div class="abs why-item" style="left:582px;top:2996px">
  <svg width="36" height="36" viewBox="0 0 36 36"><circle cx="18" cy="18" r="17" fill="none" stroke="#dfe3e8"/><rect x="12" y="10" width="12" height="16" fill="none" stroke="#5f6570"/><line x1="15" y1="15" x2="21" y2="15" stroke="#5f6570"/><line x1="15" y1="19" x2="21" y2="19" stroke="#5f6570"/></svg>
  <h4>Free Documentation</h4><p>Fundora consectetur adipiscing elit, sed do eiusmod tempor incididnt</p>
</div>
<div class="abs why-item" style="left:898px;top:2996px">
  <svg width="36" height="36" viewBox="0 0 36 36"><circle cx="18" cy="18" r="17" fill="none" stroke="#dfe3e8"/><path d="M11 18a7 7 0 1 0 3-5.7M11 11v4h4" fill="none" stroke="#5f6570" stroke-width="1.3"/></svg>
  <h4>Refinancing</h4><p>Fundora consectetur adipiscing elit, sed do eiusmod tempor incididnt</p>
</div>

<div class="abs form-col">
  <div class="heading" style="font-size:27px">Reqeust a Call Back</div>
  <p>Fundora amet sit amet, consectetur adipiscing elit, sed do eiusmod tempor incididunt ut labore et dolore magna aliqua enim ad minim veniam</p>
</div>
<div class="abs field" style="left:51px;top:3332px;width:268px">Name</div>
<div class="abs field" style="left:339px;top:3332px;width:246px">Email</div>
<div class="abs field" style="left:51px;top:3389px;width:268px">Subject</div>
<div class="abs field" style="left:339px;top:3389px;width:246px">Phone</div>
<div class="abs field" style="left:51px;top:3445px;width:534px;height:142px">Message</div>
<a class="abs btn submit">SUBMIT NOW</a>

<div class="abs faq-col">
  <div class="heading" style="font-size:27px">Frequently Ask Qustion</div>
  <p class="lead">Fundora amet sit amet, consectetur adipiscing elit, sed do eiusmod temp incididunt ut labore et dolore magna aliqua enim ad minim veniam</p>
</div>
<div class="abs faq-item open" style="left:669px;top:3332px"><span class="mark">−</span><span class="q">What kind of Financial Consultancy you need</span></div>
<p class="abs" style="left:703px;top:3360px;width:320px">Sed ut perspiciatis unde omnis iste natus error sit totam accusantium doloremque laudantium tam rem aperi eaque ipsa ab illo invet.</p>
<div class="abs faq-item" style="left:669px;top:3464px"><span class="mark">+</span><span>How we help you for your Business</span></div>
<div class="abs faq-item" style="left:669px;top:3517px"><span class="mark">+</span><span>Financial Advice</span></div>
<div class="abs faq-item" style="left:669px;top:3568px"><span class="mark">+</span><span>What is the best Business plan for you</span></div>
<div class="abs faq-item" style="left:669px;top:3622px"><span class="mark">+</span><span>Which is the right plan for Retirement</span></div>

<footer class="abs footer">
  <div class="abs col" style="left:51px;top:104px;width:260px">
    <div class="logo">KRYTOPLAN.CZ</div>
    <p style="margin-top:10px">Lorem must explain to you how all this mistaok cing pleasure and praising ain washed I will give you a complete pain was preqsain to you lorem</p>
    <div class="newsletter" style="width:252px;margin-top:24px;position:relative">Email for Newsletter
      <svg style="position:absolute;right:10px;top:9px" width="14" height="14" viewBox="0 0 14 14"><path d="M1 7l12-6-4 12-2-5z" fill="#fff"/></svg>
    </div>
  </div>
  <div class="abs col" style="left:395px;top:104px;width:210px">
    <h5>POPULAR POST</h5>
    <div style="margin-top:16px;color:#fff">Duplex Villa Design</div>
    <div>Lorem ipsum dolor sit amet, tur acmgin sed do eius</div>
    <div style="margin-top:14px;color:#fff">Real Estate Firm</div>
    <div>Lorem ipsum dolor sit amet, tur acmgin sed do eius</div>
  </div>
  <div class="abs col links" style="left:680px;top:104px;width:180px">
    <h5>QUICK LINK</h5>
    <div style="margin-top:14px">About us</div><div>Services</div><div>Projects</div><div>CASES</div><div>From Blog</div><div>Contact</div>
  </div>
  <div class="abs col" style="left:918px;top:104px;width:250px;line-height:1.9">
    <h5>CONTACT US</h5>
    <div style="margin-top:12px;padding-left:34px;position:relative"><svg style="position:absolute;left:0;top:3px" width="14" height="18" viewBox="0 0 14 18"><path d="M7 17S1 10 1 6.5a6 6 0 0 1 12 0C13 10 7 17 7 17z" fill="none" stroke="#c3cbdc"/><circle cx="7" cy="6.5" r="2" fill="none" stroke="#c3cbdc"/></svg>Riverside Lane,<br>Brno CZ</div>
    <div style="margin-top:8px;padding-left:34px;position:relative"><svg style="position:absolute;left:0;top:4px" width="14" height="14" viewBox="0 0 24 24"><path d="M5 3h4l2 5-2.5 1.5a11 11 0 0 0 6 6L16 13l5 2v4a2 2 0 0 1-2 2A16 16 0 0 1 3 5a2 2 0 0 1 2-2z" fill="none" stroke="#c3cbdc" stroke-width="2"/></svg>Telephone: (+420) 555-014-230<br>Telephone: (+420) 555-014-231</div>
    <div style="margin-top:8px;padding-left:34px">Email: hello@krytoplan.cz<br>Web: www.krytoplan.cz</div>
  </div>
  <div class="abs rule"></div>
  <div class="abs copy">Copyright© 2017 Krytoplan.cz. All rights reserved.</div>
</footer>

</body>
</html>
```